Website Redesign Project

Bright Harbor Planning provides project management and project controls consultancy services to companies in many industry sectors, within Australia and overseas. My company has been developing a business brand through forging strong business relationships within industry. We provide innovative tools, concepts and solutions to management teams to assist them in better plan and managing there project portfolios.
SECTORS OF INDUSTRY WE SERVICE
★Oil & Gas
★Minerals & Metals
★Petrochemical
★Manufacturing
★Building & Construction
★Telecommunications
★Rail
★Civil
OLD WEBSITE
My old website www.brightharborplanning.com.au needs a complete overhaul in terms of how the web pages look and feel. I am trying to get away from the grey, washed out look as it is uninviting and dull. My clients commented that my webpage does not reflect who I am as a company or my core values. Think total redesign
DESIGN
I would like a webpage design that is modern and has a corporate image. It must be elegant, classy, and have an overall glossy appearance. I want something exciting that creates some excellent feedback from clients. It needs to have a savvy appearance and an attitude of a market leader. A generic website template cannot be used as I provide a unique service to clients. I do not need a website design that looks like my compeditors, I want something that stands out in the crowd and effectivly markets my bussinesses brand. I want my website to represent quality, so only high resolution images that are clear, sharp and in focus can be used. With this design, throw your standard webpage design concepts out the window, as I want something fresh, innovative, exciting and inviting. The overall design should appear uncluttered as all content needs to be there for a reason, so think functional.
It must be professional and of the highest calibre as my clients expect nothing less. I provide clients with innovative tools, concepts and solutions, so the design needs to be edgy and creative to align with my company’s core business services. The new design must promote the company’s brand and us as a market leader. It must communicate that we service many industry sectors and reflect our company’s creativity, vision, energy and drive.
WEBPAGE WRITTEN CONTENT
I am happy with the written content on each page within my old website. You may arrange the text how you see fit within the new design. On the main page of my old website the text is under scored, I am not a big fan of this. I currently do not like the format the text is in, I am looking for a formatt that is easy to read, looks flattering and pleasing to the eye.
MAIN PAGE DESIGN
The main page design needs to focus on my company as a brand, it must promote that I service many industry sectors. My old webpage had me pigeon holed as only providing services to oil and gas. This is incorrect as I service oil & gas, metals and minerals, Petrochemical, Manufacturing, Building & Construction, Telecommunications, Rail and civil.
WEBPAGE COLUR PREFERENCE
Prefer a white background with plenty of colour
TESTIMONIAL TAB
The testimonial tab on the task bar can be removed as it is no longer required.
FINISHED PRODUCT
The finished product will be uploaded by you to a nominated web hosting account. I will need a copy of all files associated with the design. A copy of the finished product will also be provided in formats that can me imported to Xara Pro Designer as I will update my website in 6 months or so using this tool.
Updates
I have updated the design brief after recieving feedback from several designers
Thanks
Reason: Some designers have asked for more time
Hi All
I have just launched another project called "bright harbor planning business card redesign project", you are all welcome to join this project.
Thanks
Target Market(s)
★Oil and Gas
★Mining and Resources
★Building and infrastructure
★Petrochemical
★Civil and roads
★Rail
Industry/Entity Type
Industry
Requirements
Must have
- ★Draw you in
★Hold your attention
★Identify company brand
★Highlight skills experience and expertise
★Be a unique design not generic
Should not have
- ★The webpage design should not be old fashioned
★ The design should not be based off a generic design template
★The webpage should not be cluttered; everything needs to be there for a reason.

```html
<!DOCTYPE html>
<html lang="en">
<head>
<meta charset="utf-8">
<title>Bright Harbor Planning</title>
<link rel="stylesheet" href="https://fonts.googleapis.com/css2?family=Oswald:wght@500;600&family=Source+Sans+3:ital,wght@0,300;0,400;0,600;1,300;1,400&display=swap">
<style>
:root{
  --red:#e41d20;
  --red-dark:#c3080b;
  --ink:#111;
  --text:#555;
  --muted:#888;
  --line:#e2e2e2;
  --footer:#1c1c1c;
  --footer-text:#fff;
  --social:#b5b5b5;
}
*{margin:0;padding:0;box-sizing:border-box}
html,body{width:991px;height:1200px;overflow:hidden;background:#fff}
body{position:relative;font-family:"Source Sans 3",sans-serif;color:var(--text)}
.abs{position:absolute}

/* header */
.brand{left:74px;top:34px;display:flex;align-items:center;gap:10px}
.brand-mark{width:30px;height:30px;border-radius:50%;background:var(--red);flex:none}
.brand-name{font-family:"Oswald",sans-serif;font-weight:600;font-size:25px;color:var(--ink);letter-spacing:.5px;text-transform:uppercase;white-space:nowrap}
.brand-tag{left:114px;top:68px;font-size:9px;color:#333;white-space:nowrap}
.social{right:81px;top:32px;display:flex;gap:3px}
.social span{width:25px;height:25px;border-radius:50%;background:var(--social)}
.phone{right:80px;top:62px;display:flex;align-items:center;gap:4px;font-size:21px;color:#333;font-weight:400;white-space:nowrap}

/* nav */
.nav{left:75px;top:104px;width:841px;height:42px;background:linear-gradient(#ec2b2d,var(--red-dark));border-radius:6px 6px 0 0;display:flex;align-items:center}
.nav a{flex:1 1 auto;text-align:center;white-space:nowrap;font-family:"Oswald",sans-serif;font-weight:500;font-size:15px;color:#fff;text-decoration:none;text-transform:uppercase;padding:0 8px;line-height:42px;border-right:1px solid rgba(0,0,0,.18)}
.nav a:last-child{border-right:none}

/* slider */
.slider{left:75px;top:146px;width:841px;height:319px;border:1px solid var(--line);border-top:none;border-radius:0 0 6px 6px;background:#fff}
.slide{left:88px;top:156px;width:819px;height:297px;border-radius:6px;background:linear-gradient(180deg,#6a5446 0%,#8d8f98 40%,#c9ccd3 65%,#5f6670 100%)}
.dots{left:466px;top:429px;width:72px;height:24px;background:#fff;border-radius:36px 36px 0 0;display:flex;justify-content:center;align-items:center;gap:3px;padding-top:2px}
.dots i{width:6px;height:6px;border-radius:50%;background:#888}
.dots i:first-child{background:#333}

/* sectors */
.sector-band{left:75px;top:650px;width:841px;height:36px;background:linear-gradient(#fff,#f3f3f3)}
.arrow{top:528px}
.sector{top:495px;width:184px}
.sector .thumb{height:90px;border-radius:5px}
.sector h3{font-weight:300;font-size:15.5px;color:#333;margin:11px 0 3px 2px;white-space:nowrap}
.sector p{font-weight:300;font-size:11px;line-height:18px;color:var(--muted);margin-left:2px}

/* welcome */
.welcome{left:84px;top:730px;width:560px}
.welcome h1{font-weight:300;font-size:25px;color:var(--ink);line-height:30px;white-space:nowrap}
.welcome h1 strong{font-family:"Oswald",sans-serif;font-weight:500;color:var(--red);font-size:24px}
.welcome p{font-weight:300;font-size:11px;line-height:18px;margin-top:8px;color:var(--text)}
.welcome .more{display:block;margin-top:8px;font-weight:600;font-size:12.5px;color:#333;text-decoration:none}

/* testimonial */
.testi{left:668px;top:734px;width:250px}
.testi h2{font-weight:600;font-size:19px;color:var(--ink)}
.quote-mark{font-family:Georgia,serif;font-weight:700;font-size:30px;color:#444;position:absolute;left:0;top:24px;line-height:1}
.portrait{position:absolute;left:25px;top:34px;width:66px;height:63px;background:linear-gradient(#f2f2f2,#c9a98e);border:1px solid #ddd}
.testi .lead{position:absolute;left:103px;top:30px;width:146px;font-style:italic;font-weight:300;font-size:10px;line-height:16.5px;color:#666}
.testi .rest{position:absolute;left:21px;top:100px;width:228px;font-style:italic;font-weight:300;font-size:10px;line-height:16.5px;color:#666}
.testi .author{position:absolute;left:21px;top:140px;font-weight:600;font-size:10px;color:#555}

/* footer */
.ground{left:0;top:954px}
.footer{left:0;top:999px;width:991px;height:201px;background:var(--footer)}
.flinks{top:1027px;list-style:none}
.flinks li{font-family:"Oswald",sans-serif;font-weight:500;font-size:13px;color:var(--footer-text);text-transform:uppercase;line-height:23px;padding-left:11px;position:relative;white-space:nowrap}
.flinks li::before{content:"";position:absolute;left:0;top:8px;border-left:4px solid #ccc;border-top:3.5px solid transparent;border-bottom:3.5px solid transparent}
.fbrand{left:624px;top:1048px;display:flex;align-items:center;gap:9px}
.fbrand .brand-mark{background:#777;width:26px;height:26px}
.fbrand .brand-name{color:#9a9a9a;font-size:22px}
.fdivider{left:98px;top:1146px;width:795px;height:1px;background:#3b3b3b}
.copy{left:96px;top:1160px;font-weight:300;font-size:10px;color:#8a8a8a}
</style>
</head>
<body>

<header>
  <div class="abs brand"><span class="brand-mark"></span><span class="brand-name">Bright Harbor Planning</span></div>
  <div class="abs brand-tag">Providing Effective Project Controls and Management Solutions</div>
  <div class="abs social"><span></span><span></span><span></span><span></span></div>
  <div class="abs phone">
    <svg width="18" height="18" viewBox="0 0 24 24"><path d="M6.6 10.8c1.4 2.8 3.8 5.1 6.6 6.6l2.2-2.2c.3-.3.7-.4 1-.2 1.1.4 2.3.6 3.6.6.6 0 1 .4 1 1V20c0 .6-.4 1-1 1C10.6 21 3 13.4 3 4c0-.6.4-1 1-1h3.5c.6 0 1 .4 1 1 0 1.3.2 2.5.6 3.6.1.3 0 .7-.2 1z" fill="#333"/></svg>
    <span>61 0400 555 018</span>
  </div>
</header>

<nav class="abs nav">
  <a>Home</a><a>About Us</a><a>Expertise</a><a>Knowledge</a><a>Experience</a><a>Projects</a><a>Focus</a><a>Contact</a><a>Recruitment</a>
</nav>

<div class="abs slider"></div>
<div class="abs slide" role="img" aria-label="Photo of an industrial plant interior with white pressure vessels and piping"></div>
<div class="abs dots"><i></i><i></i><i></i><i></i></div>

<div class="abs sector-band"></div>
<svg class="abs arrow" style="left:80px" width="16" height="28" viewBox="0 0 16 28"><path d="M13 2 3 14l10 12" fill="none" stroke="#999" stroke-width="2"/></svg>
<svg class="abs arrow" style="left:893px" width="16" height="28" viewBox="0 0 16 28"><path d="M3 2l10 12L3 26" fill="none" stroke="#999" stroke-width="2"/></svg>

<section class="abs sector" style="left:106px">
  <div class="thumb" role="img" aria-label="Photo of white oil and gas pipelines" style="background:linear-gradient(#3f7fd0 0%,#dfe8f2 45%,#eef0f2 70%,#5a9a3a 100%)"></div>
  <h3>Oil &amp; Gas</h3>
  <p>Nunc tempus felis vitae urna. Vivam us porttitor purus nisi eleifend</p>
</section>
<section class="abs sector" style="left:304px">
  <div class="thumb" role="img" aria-label="Photo of metal processing machinery in a plant" style="background:linear-gradient(90deg,#5c6b78,#b7c2cb 50%,#3d6a9a)"></div>
  <h3>Minerals &amp; Metals</h3>
  <p>Nunc tempus felis vitae urna. Vi portti- tor purus nisi eleifend</p>
</section>
<section class="abs sector" style="left:501px">
  <div class="thumb" role="img" aria-label="Photo of a petrochemical facility with silos under blue sky" style="background:linear-gradient(#6fa3dc 0%,#c9dcef 45%,#9aa0a6 75%,#4a4f55 100%)"></div>
  <h3>Petrochemical</h3>
  <p>Nunc tempus felis vitae urna. Viva- mus porttitor purus nisi eleifend</p>
</section>
<section class="abs sector" style="left:699px">
  <div class="thumb" role="img" aria-label="Photo of manufactured metal parts on a production line" style="background:linear-gradient(#d45a3a 0%,#c8ccd2 40%,#9aa6b4 100%)"></div>
  <h3>Manufacturing</h3>
  <p>Nunc tempus felis vitae urna. Vivamus porttitor purus nisi eleifend</p>
</section>

<section class="abs welcome">
  <h1>WELCOME TO <strong>BRIGHT HARBOR PLANNING</strong></h1>
  <p>I provide services to companies in the mining and oil and gas sector to enabling them to plan and manage their construction projects more effectively. This is achieved by evaluating the businesses practices and them implementing different tools and solutions.</p>
  <p>My clients are then able to plan and deliver their projects, on time and within their budgets. I am able to provide services to both large and small scale businesses within Australian and Overseas. I offer my clients value by providing, exceptional skills and expertise at a competitive market rate.</p>
  <a class="more">Learn More</a>
</section>

<aside class="abs testi">
  <h2>Testimonials</h2>
  <span class="quote-mark">&ldquo;</span>
  <div class="portrait" role="img" aria-label="Portrait photo of a smiling client"></div>
  <p class="lead">Nunc tempus felis vitae urna. Vivamus porttitor, neque at volut- pat rutrum, purus nisi eleifend libero, a tempus libero lectus</p>
  <p class="rest">Morbi eget arcu. Morbi porta, libero id ullamcorper nonummy, nibh ligula pulvinar metus &rdquo;</p>
  <p class="author">By Author Name</p>
</aside>

<svg class="abs ground" width="991" height="46" viewBox="0 0 991 46" preserveAspectRatio="none">
  <path d="M0 46V36l20-6 25 4 30-8 40 10 50-5 45 3 30-9 40 8 55-4 40 6 45-10 50 9 40-3 45 5 50-11 40 7 45-2 40 6 50-9 45 8 40-4 50 6 45-10 40 9 50-3 V46Z" fill="var(--footer)"/>
</svg>
<div class="abs footer"></div>

<ul class="abs flinks" style="left:98px"><li>Home</li><li>About Us</li><li>Expertise</li><li>Knowledge</li></ul>
<ul class="abs flinks" style="left:211px"><li>Experience</li><li>Projects</li><li>Focus</li></ul>
<ul class="abs flinks" style="left:325px"><li>Recruitment</li><li>Contact</li></ul>

<div class="abs fbrand"><span class="brand-mark"></span><span class="brand-name">Bright Harbor Planning</span></div>

<div class="abs fdivider"></div>
<p class="abs copy">&copy; 2013 Company Name.&nbsp; All right reserved. Term of Use</p>

</body>
</html>
```